Stationery Design Project - Ma clairiere

We are a french company, Ma Clairiere. It means My Glade.
We own and manage woods, we transform it industrially into very high quality (dry) logs and pellets and we commercialize them to individuals in France.
People can order the logs online or by phone and get the wood logs delivered at home.

After our great logo contest, we would like to launch a new stationery project.
Updates

Target Market(s)

inhabitants of sub-urban areas in France. (living in houses not in apartment )

Industry/Entity Type

It Company

Requirements
Must have
• content see attachment
logo

For the business card, we would like on the front side, the logo, name + contact info. We would like to use the back side for commercial purpose insisting on our distinctive value proposition.
Nice to have
• the back side of the business card can be more colorful

```html
<!DOCTYPE html>
<html lang="fr">
<head>
<meta charset="utf-8">
<title>Ma Clairiere – cartes de visite</title>
<link href="https://fonts.googleapis.com/css2?family=Montserrat:wght@400;500;600;700;800&display=swap" rel="stylesheet">
<style>
  :root {
    --backdrop: #2b2b2d;
    --card-white: #f4f4f4;
    --card-grey: #d9d9d9;
    --brand-red: #c8102e;
    --brand-red-dark: #8e0a1f;
    --ink: #2a2a2a;
    --ink-soft: #4a4a4a;
    --white: #ffffff;
  }
  * { box-sizing: border-box; margin: 0; padding: 0; }
  html, body { width: 1200px; height: 901px; overflow: hidden; }
  body {
    background: var(--backdrop);
    font-family: "Montserrat", sans-serif;
    position: relative;
  }
  .card {
    position: absolute;
    top: 130px;
    width: 420px;
    height: 640px;
    border-radius: 28px;
    overflow: hidden;
    box-shadow: 0 18px 40px rgba(0,0,0,0.45);
  }

  /* Back side */
  .card--back {
    left: 150px;
    background: linear-gradient(160deg, var(--brand-red) 0%, #b00d27 60%, var(--brand-red-dark) 100%);
    color: var(--white);
  }
  .card--back .wordmark {
    position: absolute;
    left: 50px;
    top: 608px;
    transform: rotate(-90deg);
    transform-origin: left top;
    font-size: 72px;
    line-height: 1;
    font-weight: 700;
    letter-spacing: -2px;
    color: var(--white);
    white-space: nowrap;
  }
  .card--back .mascot {
    position: absolute;
    left: 170px;
    top: 40px;
    width: 200px;
    height: 300px;
    border-radius: 14px;
    background: linear-gradient(180deg, #d9b99a 0%, #b3202e 40%, #2f4a78 80%, #6b4428 100%);
  }
  .card--back .pitch {
    position: absolute;
    left: 170px;
    top: 365px;
    width: 225px;
    font-size: 14px;
    font-weight: 500;
    line-height: 1.35;
  }
  .card--back .pitch p + p { margin-top: 14px; }
  .nowrap { white-space: nowrap; }

  /* Front side */
  .card--front {
    left: 630px;
    background: linear-gradient(180deg, var(--card-white) 0%, var(--card-grey) 100%);
    color: var(--ink);
    text-align: center;
  }
  .card--front .wordmark {
    margin-top: 48px;
    padding-left: 26px;
    text-align: left;
    font-size: 42px;
    font-weight: 700;
    letter-spacing: -1.5px;
    color: var(--ink);
  }
  .card--front .holder {
    margin-top: 14px;
    font-size: 21px;
    font-weight: 500;
    color: var(--ink-soft);
  }
  .card--front .holder .surname { color: var(--brand-red); }
  .contact { margin-top: 18px; }
  .contact .label {
    display: block;
    font-size: 12px;
    font-weight: 600;
    color: var(--brand-red);
    margin-top: 6px;
  }
  .contact .value {
    display: block;
    font-size: 19px;
    font-weight: 500;
    color: var(--ink);
  }
  .card--front .mascot {
    position: absolute;
    left: 60px;
    bottom: 0;
    width: 320px;
    height: 230px;
    border-radius: 14px 14px 0 0;
    background: linear-gradient(180deg, #c8a98c 0%, #b3202e 55%, #7d1420 100%);
  }
</style>
</head>
<body>
  <section class="card card--back" aria-label="Verso de la carte">
    <div class="wordmark">Ma Clairiere</div>
    <div class="mascot" role="img" aria-label="Illustration d'un bûcheron en chemise à carreaux portant un plateau de bûches"></div>
    <div class="pitch">
      <p>Livraison gratuite de bois de chauffage à Lyon et région. Bûches, granulés, briquettes.</p>
      <p>Commandez sur www.maclairiere.fr ou au <span class="nowrap">04 72 10 20 30</span></p>
      <p>Qualité supérieure, origine France certifiée.</p>
    </div>
  </section>

  <section class="card card--front" aria-label="Recto de la carte">
    <div class="wordmark">Ma Clairiere</div>
    <div class="holder">Pierre-Antoine <span class="surname">LAVAL</span></div>
    <div class="contact">
      <span class="label">Tél:</span>
      <span class="value">04 72 10 20 30</span>
      <span class="label">Mobile:</span>
      <span class="value">04 72 10 20 30</span>
      <span class="label">Email:</span>
      <span class="value">laval@maclairiere.fr</span>
      <span class="label">Du bois sec, livré chez vous!</span>
      <span class="value">www.maclairiere.fr</span>
    </div>
    <div class="mascot" role="img" aria-label="Illustration d'un bûcheron musclé en chemise à carreaux tenant un plateau de bûches"></div>
  </section>
</body>
</html>
```